Business card for Full Stable Care Vandorpe

I would like to have me designed an professional business card with my existing logo for my company called : full stable care vandorpe gcv.
I prefer a two sided business card with on the back side only the horses head and the website : fscvandorpe-example.eu
Only one colour shouldbe all right.
The logo must appear in a nic professional way on the business card.

Other suggestion are welcome.

All copy wrights must be released by the designer after we have selected a final design.

Target Market(s)

Equestrian businesses

Industry/Entity Type

Business

Contact Information for Business Card

Laurent Vandorpe
Title: zaakvoerder
Full Stable Care Vandorpe GCV
Molkenweg 47
B - 2890 Velddorp
België
Phone: + 32 491 68 27 04
Mail: laurent@fscvandorpe-example.eu

Font styles to use
Serif

Requirements
Must have
• My own logo
• See attached files
• Website: fscvandorpe-example.eu

```html
<!DOCTYPE html>
<html lang="nl">
<head>
<meta charset="utf-8">
<title>Full Stable Care Vandorpe – visitekaartje</title>
<link rel="stylesheet" href="https://fonts.googleapis.com/css2?family=Tinos:wght@400;700&display=swap">
<style>
  :root {
    --backdrop: #e6e2dc;
    --card: #060606;
    --silver: #dcdcdc;
    --silver-soft: #c4c4c4;
    --mark-grey: #7a7a7a;
    --web-grey: #3c3c3c;
    --rule: #8d8d8d;
  }
  * { box-sizing: border-box; margin: 0; padding: 0; }
  html, body { width: 1200px; height: 913px; overflow: hidden; background: var(--backdrop); }
  body { position: relative; font-family: "Tinos", "Times New Roman", serif; color: var(--silver); }

  .card {
    position: absolute;
    width: 560px;
    height: 340px;
    background: var(--card);
    box-shadow: 0 14px 30px rgba(0,0,0,0.35);
  }
  .card--back { left: 50px; top: 70px; }
  .card--front { left: 590px; top: 503px; }

  /* back side */
  .back-brand {
    position: absolute;
    left: 0; right: 0; top: 80px;
    display: flex; flex-direction: column; align-items: center; gap: 14px;
  }
  .back-brand__dot { width: 64px; height: 64px; border-radius: 50%; background: var(--mark-grey); }
  .back-brand__name { font-weight: 700; font-size: 24px; color: var(--mark-grey); }
  .back-web {
    position: absolute; left: 0; right: 0; top: 250px;
    text-align: center; font-weight: 700; font-size: 22px; color: var(--web-grey);
  }

  /* front side */
  .front-brand {
    position: absolute; left: 34px; top: 84px;
    display: flex; align-items: center; gap: 12px;
  }
  .front-brand__dot { width: 36px; height: 36px; border-radius: 50%; background: var(--silver); }
  .front-brand__name { font-weight: 700; font-size: 21px; line-height: 1.1; color: var(--silver); width: 180px; }

  .holder { position: absolute; right: 30px; top: 96px; text-align: right; }
  .holder__name { font-weight: 700; font-size: 23px; color: var(--silver); line-height: 1.1; }
  .holder__title { font-size: 17px; color: var(--silver-soft); line-height: 1.2; }

  .divider { position: absolute; left: 30px; right: 30px; top: 152px; height: 1px; background: var(--rule); }

  .address {
    position: absolute; right: 30px; top: 166px;
    text-align: right; font-size: 18px; line-height: 1.3; font-style: normal;
  }

  .contact { position: absolute; left: 30px; top: 240px; font-size: 17px; line-height: 1.55; }
  .contact__row { display: flex; align-items: center; gap: 8px; }
  .contact__row svg { width: 16px; height: 16px; flex: none; }
</style>
</head>
<body>

  <section class="card card--back" aria-label="Achterkant">
    <div class="back-brand">
      <span class="back-brand__dot" aria-hidden="true"></span>
      <span class="back-brand__name">Full Stable Care Vandorpe</span>
    </div>
    <p class="back-web">fscvandorpe-example.eu</p>
  </section>

  <section class="card card--front" aria-label="Voorkant">
    <div class="front-brand">
      <span class="front-brand__dot" aria-hidden="true"></span>
      <span class="front-brand__name">Full Stable Care Vandorpe</span>
    </div>

    <div class="holder">
      <p class="holder__name">Laurent Vandorpe</p>
      <p class="holder__title">zaakvoerder</p>
    </div>

    <div class="divider"></div>

    <address class="address">
      Molkenweg 47<br>
      B - 2890 Velddorp<br>
      België
    </address>

    <div class="contact">
      <p class="contact__row">
        <svg viewBox="0 0 16 16" aria-hidden="true"><circle cx="8" cy="8" r="7" fill="none" stroke="#dcdcdc" stroke-width="1"/><path d="M5.5 4.5l1.5 1.5-1 1c.6 1.2 1.5 2.1 2.7 2.7l1-1 1.5 1.5-1 1.2C7.6 11 5 8.4 4.6 5.8z" fill="#dcdcdc"/></svg>
        + 32 491 68 27 04
      </p>
      <p class="contact__row">
        <svg viewBox="0 0 16 16" aria-hidden="true"><rect x="1.5" y="3.5" width="13" height="9" fill="none" stroke="#dcdcdc" stroke-width="1"/><path d="M1.5 3.5L8 9l6.5-5.5" fill="none" stroke="#dcdcdc" stroke-width="1"/></svg>
        laurent@fscvandorpe-example.eu
      </p>
    </div>
  </section>

</body>
</html>
```